Create a Brochure Design for Brantley Homecare

Brantley Homecare is a subsidiary of the Brantley Care Group. This brochure is specifically for the Brantley Homecare company and brand. Create a 3 panel, A4, front and back, tri-fold brochure. This brochure will be a way to introduce our Homecare services to the community, prospective clients, and various referral partners. The brochure must be eye catching, unique in its deliverables and demonstrate both attention to detail and comfort. Our organization is sophisticated and built around warmth, care and individualized personal attention. The most important aspect of this design is to focus on creating a nurturing, warm, and inviting feel where you would want to have a Nurse or Nurse’s Aide in your own home or a loved one’s home.

I am open to the creativity of the designer to develop something based on the above criteria; however I would like the design to work well with the existing collateral material. What I mean by that is that while I want everything to have its own personality and stand out as its own brand representative, I still need to be able to tell that the overall design concept stays stylistically inside of the same ‘family’ of existing designed material. Because of this, below I would like for the designer to pull inspiration from the link to our website (Located below) as well as from the attachment of our recently refreshed business cards (Attached). This should allow each design to be unique and creative, while still staying inside of a framework and the feel/style that I am looking for.

Finally, I want all the designers to understand that this brochure design is for a private, in home, healthcare company where we are responsible for providing personalized care for a culturally and ethnically diverse make-up clientele of all ages. The photos that are used must represent an image of warmth, care, and a positive interaction between client and caregiver.

Look under the Brantley Homecare tab at www.brantleycaregroup-example.net

Industry/Entity Type

Healthcare

Requirements
Must have
• • The Brantley Homecare company logo must be included.

```html
<!DOCTYPE html>
<html lang="en">
<head>
<meta charset="utf-8">
<title>Brantley Homecare Brochure</title>
<link href="https://fonts.googleapis.com/css2?family=Marcellus&family=Cormorant+Garamond:ital,wght@1,500&family=Lato:wght@400;700&display=swap" rel="stylesheet">
<style>
  :root {
    --stage: #d9dadb;
    --teal: #1f6f68;
    --teal-deep: #144f4a;
    --teal-light: #2a847b;
    --rose: #e88a8f;
    --rose-soft: #f2b9bb;
    --paper: #ffffff;
    --ink: #3c3c3c;
    --ink-soft: #6a6a6a;
    --photo-warm: #cdb9a4;
    --photo-cool: #9fb7b0;
    --photo-green: #8aa36a;
  }
  * { box-sizing: border-box; margin: 0; padding: 0; }
  html, body { width: 1200px; height: 900px; overflow: hidden; }
  body {
    background: var(--stage);
    font-family: "Lato", sans-serif;
    color: var(--ink);
    position: relative;
  }
  .panel { position: absolute; box-shadow: 0 4px 14px rgba(0,0,0,.18); }

  /* Front cover */
  .cover {
    left: 40px; top: 40px; width: 540px; height: 380px;
    background: linear-gradient(160deg, var(--teal-light), var(--teal) 45%, var(--teal-deep));
    overflow: hidden;
  }
  .cover-window {
    position: absolute; left: 44px; top: 64px; width: 220px; height: 260px;
    border-radius: 26px;
    background: linear-gradient(135deg, var(--photo-cool), var(--photo-warm) 55%, var(--photo-green));
  }
  .cover-tagline {
    position: absolute; left: 300px; top: 150px;
    font-family: "Marcellus", serif; color: var(--paper);
  }
  .cover-tagline .lead { display: block; font-size: 30px; line-height: 1; }
  .cover-tagline .big { display: block; font-size: 78px; line-height: 1; letter-spacing: 1px; margin-top: 6px; }
  .brand-mark {
    display: flex; align-items: center; gap: 6px;
    font-family: "Marcellus", serif; white-space: nowrap;
  }
  .brand-mark .dot { width: 12px; height: 12px; background: currentColor; flex: none; }
  .cover .brand-mark { position: absolute; right: 18px; top: 16px; color: var(--paper); font-size: 13px; }

  /* Back cover */
  .back {
    left: 620px; top: 40px; width: 540px; height: 380px;
    background: var(--paper);
  }
  .back-marks {
    position: absolute; left: 0; right: 0; top: 172px;
    display: flex; justify-content: center; gap: 22px; font-size: 13px;
  }
  .mark-group { color: #2b2b2b; }
  .mark-homecare { color: var(--rose); }
  .mark-sanctuary { color: var(--teal-light); }

  /* Inside spread */
  .inside {
    left: 40px; top: 460px; width: 1120px; height: 400px;
    display: flex;
  }
  .inside-flap { width: 150px; background: linear-gradient(160deg, var(--teal-light), var(--teal-deep)); }
  .inside-main { width: 560px; background: var(--paper); position: relative; }
  .inside-services { width: 410px; background: var(--rose); position: relative; color: var(--paper); padding: 26px 30px; }

  .photo { position: absolute; background: linear-gradient(135deg, var(--photo-warm), var(--photo-cool)); }
  .photo.green { background: linear-gradient(135deg, var(--photo-green), var(--photo-warm)); }

  .intro {
    position: absolute; left: 372px; top: 30px; width: 166px;
    font-size: 9px; line-height: 1.45; color: var(--ink-soft);
  }
  .intro .brand-mark { color: var(--rose); font-size: 12px; margin-bottom: 12px; }
  .intro p { margin-bottom: 8px; }
  .intro ul { list-style: none; margin-bottom: 8px; }
  .intro li::before { content: "– "; color: var(--rose); }
  .intro .web { color: var(--teal); font-weight: 700; word-break: break-all; }

  .services-title {
    font-family: "Cormorant Garamond", serif; font-style: italic; font-weight: 500;
    font-size: 30px; line-height: 1; margin-bottom: 10px;
  }
  .services p { font-size: 9.5px; line-height: 1.5; margin-bottom: 7px; }
  .services strong { font-weight: 700; }
  .service-strip {
    height: 56px; margin: 10px 0 12px;
    background: linear-gradient(90deg, var(--photo-warm), var(--rose-soft) 50%, var(--photo-cool));
  }
</style>
</head>
<body>

  <section class="panel cover" aria-label="Front cover">
    <div class="brand-mark"><span class="dot"></span>Brantley Care Group</div>
    <div class="cover-window" role="img" aria-label="Window of caregiver photos: nurses with elderly clients and hands held together"></div>
    <h1 class="cover-tagline"><span class="lead">we're here to</span><span class="big">HELP.</span></h1>
  </section>

  <section class="panel back" aria-label="Back cover">
    <div class="back-marks">
      <div class="brand-mark mark-group"><span class="dot"></span>Brantley Care Group</div>
      <div class="brand-mark mark-homecare"><span class="dot"></span>Brantley Homecare</div>
      <div class="brand-mark mark-sanctuary"><span class="dot"></span>Brantley Sanctuary</div>
    </div>
  </section>

  <section class="panel inside" aria-label="Inside spread">
    <div class="inside-flap"></div>

    <div class="inside-main">
      <div class="photo" style="left:20px;top:30px;width:80px;height:110px" role="img" aria-label="Nurse with an elderly man"></div>
      <div class="photo" style="left:20px;top:150px;width:80px;height:110px" role="img" aria-label="Doctor checking an elderly man"></div>
      <div class="photo green" style="left:20px;top:270px;width:80px;height:100px" role="img" aria-label="Caregiver walking with a client outdoors"></div>
      <div class="photo" style="left:108px;top:20px;width:140px;height:110px" role="img" aria-label="Nurse helping a man in bed"></div>
      <div class="photo" style="left:108px;top:138px;width:140px;height:110px" role="img" aria-label="Hands held together in comfort"></div>
      <div class="photo" style="left:108px;top:256px;width:140px;height:114px" role="img" aria-label="Caregiver supporting a man with a walker"></div>
      <div class="photo" style="left:256px;top:40px;width:90px;height:90px" role="img" aria-label="Caregiver bringing a breakfast tray"></div>
      <div class="photo" style="left:256px;top:138px;width:90px;height:110px" role="img" aria-label="Client taking medicine with a glass of water"></div>
      <div class="photo green" style="left:256px;top:256px;width:90px;height:114px" role="img" aria-label="Nurse walking with an elderly woman in a garden"></div>

      <div class="intro">
        <div class="brand-mark"><span class="dot"></span>Brantley Homecare</div>
        <p>Brantley Homecare brings trusted nursing and personal care into the comfort of your own home.</p>
        <p>Our caregivers are carefully chosen, trained and supported so every visit feels warm, calm and personal.</p>
        <p>We listen first, then build a plan around the routines, wishes and pace of each client.</p>
        <p>We can help with:</p>
        <ul>
          <li>Bathing and dressing</li>
          <li>Meals and medication</li>
          <li>Companionship</li>
          <li>Light housekeeping</li>
          <li>Respite for families</li>
        </ul>
        <p>Visit <span class="web">www.brantleycaregroup-example.net</span> to learn more.</p>
      </div>
    </div>

    <div class="inside-services services">
      <h2 class="services-title">Services</h2>
      <p>Every care plan begins with a home visit from our nurse to understand what matters most to you.</p>
      <div class="service-strip" role="img" aria-label="Strip of photos showing caregivers with clients of different ages"></div>
      <p><strong>Personal Care:</strong> help with daily routines, given with patience and respect.</p>
      <p><strong>Skilled Nursing:</strong> wound care, medication support and health checks at home.</p>
      <p><strong>Respite Care:</strong> short breaks for family carers, day or night.</p>
      <p><strong>Flexible Schedules:</strong> a few hours a week or around-the-clock support.</p>
    </div>
  </section>

</body>
</html>
```